Website Design for Dorrint.com

We are starting up a business to sell Blutooth devices. Initially speakers and headphones

Dorrint of Norway
Leading technology, uncompromised quality.

Specialist in top quality bluetooth equipment
We specialize in design and production of top

```html
<!DOCTYPE html>
<html lang="en">
<head>
<meta charset="utf-8">
<title>Dorrint of Norway – Bluetooth Speakers</title>
<link rel="stylesheet" href="https://fonts.googleapis.com/css2?family=Raleway:wght@300;400&family=Open+Sans:ital,wght@0,400;0,600;1,700&display=swap">
<style>
  :root {
    --page-bg: #ffffff;
    --ink: #4a4a4a;
    --ink-soft: #7a7a7a;
    --rule: #d2d2d2;
    --nav-top: #6b6b6b;
    --nav-bottom: #3a3a3a;
    --panel-top: #f4f4f4;
    --panel-bottom: #c9c9c9;
    --signup-frame: #d6d6d6;
    --signup-bg: #1e1e1e;
    --field-bg: #f2f2f2;
    --field-ink: #9a9a9a;
    --go-top: #f3c46a;
    --go-bottom: #c7831c;
    --footer-ink: #eeeeee;
  }
  * { box-sizing: border-box; margin: 0; padding: 0; }
  html, body { width: 1200px; height: 885px; overflow: hidden; background: var(--page-bg); }
  .page { position: relative; width: 1200px; height: 885px; font-family: "Open Sans", Arial, sans-serif; color: var(--ink); }

  /* header */
  .brand { position: absolute; left: 262px; top: 44px; color: #555; font-family: "Raleway", Arial, sans-serif; font-weight: 400; text-align: right; }
  .brand-name { font-size: 46px; line-height: 1; letter-spacing: 1px; }
  .brand-sub { font-size: 16px; letter-spacing: 2px; margin-top: 2px; }

  .main-nav { position: absolute; left: 520px; top: 49px; width: 464px; height: 47px; border-radius: 7px; background: linear-gradient(var(--nav-top), var(--nav-bottom)); display: flex; box-shadow: 0 2px 3px rgba(0,0,0,.3); }
  .main-nav a { flex: 1; color: #fff; text-decoration: none; font-size: 13px; font-weight: 600; letter-spacing: 1.5px; display: flex; align-items: center; justify-content: center; border-right: 1px solid #2e2e2e; box-shadow: inset -1px 0 0 #777; }
  .main-nav a:last-child { border-right: none; box-shadow: none; }
  .nav-reflection { position: absolute; left: 520px; top: 98px; width: 464px; height: 36px; border-radius: 0 0 7px 7px; background: linear-gradient(rgba(0,0,0,.12), rgba(0,0,0,0)); }

  /* hero */
  .guide { position: absolute; background: var(--rule); }
  .hero-visual { position: absolute; left: 205px; top: 150px; width: 488px; height: 370px; background: radial-gradient(ellipse at 50% 55%, #e6e6e6 0%, #f6f6f6 55%, #ffffff 80%); }
  .hero-title { position: absolute; left: 745px; top: 186px; font-family: "Raleway", Arial, sans-serif; font-weight: 300; font-size: 58px; letter-spacing: 3px; color: #555; }
  .hero-subtitle { position: absolute; left: 747px; top: 246px; font-family: "Raleway", Arial, sans-serif; font-weight: 300; font-size: 20px; color: #6a6a6a; }
  .hero-copy { position: absolute; left: 747px; top: 277px; width: 226px; font-size: 12px; line-height: 17.5px; color: var(--ink-soft); }
  .btn-read { position: absolute; left: 747px; top: 416px; width: 102px; height: 37px; border-radius: 6px; background: linear-gradient(#5a5a5a, #262626); color: #eee; font-family: "Raleway", Arial, sans-serif; font-size: 15px; display: flex; align-items: center; justify-content: center; box-shadow: 0 3px 4px rgba(0,0,0,.35); }

  .footer-wave { position: absolute; left: 0; top: 715px; }

  /* info panels */
  .info-panel { position: absolute; top: 551px; width: 251px; height: 205px; background: linear-gradient(var(--panel-top), var(--panel-bottom)); box-shadow: 0 6px 8px rgba(0,0,0,.35); padding: 10px 12px; }
  .info-panel h2 { font-family: "Raleway", Arial, sans-serif; font-weight: 300; font-size: 26px; letter-spacing: 3px; text-align: center; color: #777; padding-bottom: 6px; border-bottom: 1px solid #bdbdbd; margin-bottom: 10px; }
  .info-panel p { font-size: 12.3px; line-height: 18px; color: #4a4a4a; }
  .panel-who { left: 216px; }
  .panel-quality { left: 476px; }

  .signup { position: absolute; left: 737px; top: 551px; width: 251px; height: 205px; background: var(--signup-frame); padding: 8px 9px; }
  .signup-inner { width: 100%; height: 100%; background: var(--signup-bg); position: relative; }
  .signup h2 { position: absolute; left: 26px; top: 12px; font-style: italic; font-weight: 700; font-size: 27px; color: #fff; }
  .field { position: absolute; left: 10px; width: 211px; height: 24px; background: var(--field-bg); border: 1px solid #bbb; font-size: 12px; font-style: italic; color: var(--field-ink); padding: 3px 7px; }
  .field-name { top: 53px; }
  .field-email { top: 84px; }
  .field-country { top: 114px; }
  .field-country::after { content: ""; position: absolute; right: 0; top: 0; width: 22px; height: 22px; background: #d0d0d0; }
  .field-arrow { position: absolute; right: 5px; top: 7px; z-index: 1; }
  .btn-go { position: absolute; left: 67px; top: 148px; width: 102px; height: 29px; border-radius: 5px; background: linear-gradient(var(--go-top), var(--go-bottom)); color: #fff; font-weight: 700; font-style: italic; font-size: 13px; display: flex; align-items: center; justify-content: center; border: 1px solid #9a5f10; }

  /* footer */
  .footer-nav { position: absolute; left: 588px; top: 814px; width: 280px; display: flex; justify-content: space-between; font-size: 9.5px; letter-spacing: 1.3px; color: var(--footer-ink); }
  .copyright { position: absolute; right: 332px; top: 830px; font-size: 8.5px; letter-spacing: 1.2px; color: var(--footer-ink); white-space: nowrap; }
  .footer-brand { position: absolute; left: 884px; top: 806px; color: var(--footer-ink); font-family: "Raleway", Arial, sans-serif; text-align: right; }
  .footer-brand .brand-name { font-size: 24px; letter-spacing: 1px; }
  .footer-brand .brand-sub { font-size: 9px; letter-spacing: 1px; margin-top: 0; }
</style>
</head>
<body>
<div class="page">

  <header>
    <div class="brand">
      <div class="brand-name">Dorrint</div>
      <div class="brand-sub">of Norway</div>
    </div>
    <nav class="main-nav">
      <a href="#">Home</a>
      <a href="#">About us</a>
      <a href="#">Contact</a>
      <a href="#">Products</a>
    </nav>
    <div class="nav-reflection"></div>
  </header>

  <section class="hero">
    <span class="guide" style="left:187px;top:120px;width:1px;height:213px"></span>
    <span class="guide" style="left:175px;top:137px;width:253px;height:1px"></span>
    <span class="guide" style="left:723px;top:373px;width:1px;height:147px"></span>
    <span class="guide" style="left:667px;top:497px;width:173px;height:1px"></span>
    <div class="hero-visual" role="img" aria-label="Product photo of three rounded Bluetooth speakers, two glossy white and one black"></div>
    <h1 class="hero-title">D100</h1>
    <div class="hero-subtitle">BLUETOOTH SPEAKER</div>
    <p class="hero-copy">A very small high-quality Bluetooth speaker device that advanced speaker design and powered isolation technology to their subtle, slick aesthetic, they produce that high definition listening experience you thought couldn't be achieved by other bluetooth speakers.</p>
    <a class="btn-read">Read More</a>
  </section>

  <svg class="footer-wave" width="1200" height="170" viewBox="0 0 1200 170">
    <defs>
      <linearGradient id="footerFill" x1="0" y1="0" x2="0" y2="1">
        <stop offset="0" stop-color="#5a5a5a"/>
        <stop offset="0.35" stop-color="#6f6f6f"/>
        <stop offset="1" stop-color="#a3a3a3"/>
      </linearGradient>
    </defs>
    <path d="M0 30 Q600 125 1200 35 L1200 170 L0 170 Z" fill="url(#footerFill)"/>
    <path d="M0 48 Q600 140 1200 52" fill="none" stroke="#8a8a8a" stroke-width="1"/>
  </svg>

  <section class="info-panel panel-who">
    <h2>Who We Are</h2>
    <p>Specialist in top quality bluetooth equipment<br>We specialize in design and production of top quality bluetooth equipment and we make it available to the world market at a reasonable price based on the shortest possible route from manu-facturing to the consumer.</p>
  </section>

  <section class="info-panel panel-quality">
    <h2>Our Quality</h2>
    <p>Our business concept is based on opti-mizing design, functionality and quality assurance in making top of the line products available to our customers. Norwegians have for generations rep-resented some of the worlds most de-manding customers requiring the high-est quality of the products consumed.</p>
  </section>

  <section class="signup">
    <div class="signup-inner">
      <h2>Sign up now!</h2>
      <div class="field field-name">Name</div>
      <div class="field field-email">Email address</div>
      <div class="field field-country">Select Country
        <svg class="field-arrow" width="10" height="8" viewBox="0 0 10 8"><path d="M0 0 H10 L5 8 Z" fill="#777"/></svg>
      </div>
      <a class="btn-go">GO !</a>
    </div>
  </section>

  <footer>
    <nav class="footer-nav">
      <span>Home</span><span>|</span><span>About us</span><span>|</span><span>Contact</span><span>|</span><span>Products</span>
    </nav>
    <p class="copyright">Copyright © DORRINT OF NORWAY 2012. All rights reserved.</p>
    <div class="footer-brand">
      <div class="brand-name">Dorrint</div>
      <div class="brand-sub">of Norway</div>
    </div>
  </footer>

</div>
</body>
</html>
```